Merrowind Flyer

A simple flyer that gets people attention
I have a attached a sample of what we use now and a picture we use
We service gas fireplaces and need a eye catching but not to cluttered flyer to promote our business. the cost per fireplace should be $60.00

Reason: Sorry for the delay We are out of town on holidays with sketchy internet service To frustrating to complete this project till I am back in a week Thank you for your patience Kind regards Dale

```html
<!DOCTYPE html>
<html lang="en">
<head>
<meta charset="utf-8">
<title>Merrowind Gas Services Flyer</title>
<link href="https://fonts.googleapis.com/css2?family=Open+Sans:wght@400;600;700&family=Oswald:wght@500;600&display=swap" rel="stylesheet">
<style>
:root{
  --bg:#0b0806;
  --ink:#ffffff;
  --flame:#f0782a;
  --flame-deep:#d9541a;
  --panel:rgba(255,255,255,0.86);
  --panel-ink:#1c1c1c;
  --band:rgba(20,14,10,0.78);
  --muted:#b9b0a8;
  --badge:#c8102e;
}
*{margin:0;padding:0;box-sizing:border-box}
html,body{width:849px;height:1200px;overflow:hidden;background:var(--bg)}
body{font-family:"Open Sans",Arial,sans-serif;color:var(--ink)}
.flyer{position:relative;width:849px;height:1200px;overflow:hidden;background:var(--bg)}
.scene{position:absolute;left:0;top:150px;width:849px;height:900px;
  background:
    radial-gradient(ellipse 420px 170px at 560px 200px, rgba(255,150,40,.85), rgba(200,70,10,.45) 55%, transparent 80%),
    radial-gradient(ellipse 520px 280px at 430px 760px, #d99a78, #a86448 45%, rgba(60,30,20,.6) 75%, transparent 95%),
    linear-gradient(#140c06 0%, #2a150a 35%, #3a2014 60%, #1a0e08 100%);}
.header{position:absolute;left:18px;top:14px;display:flex;gap:18px;align-items:flex-start}
.brand-mark{width:104px;height:104px;background:var(--flame-deep)}
.brand-text{padding-top:12px}
.brand-name{font-family:"Oswald",Arial,sans-serif;font-weight:600;font-size:31px;line-height:1.1;color:var(--flame);letter-spacing:1px;text-transform:uppercase}
.tagline{font-size:25px;line-height:1.2;color:var(--ink);margin-top:4px;width:660px}
.rule{position:absolute;left:0;top:236px;width:849px;height:1px;background:rgba(255,255,255,.35)}
.intro{position:absolute;left:40px;top:250px;width:769px;text-align:center;font-size:17px;line-height:1.3}
.intro p+p{margin-top:20px}
.service-panel{position:absolute;left:150px;top:458px;width:676px;padding:12px 18px 14px;background:var(--panel);color:var(--panel-ink);font-size:14.5px;line-height:1.35}
.agency{display:flex;align-items:center;gap:12px;margin-bottom:12px}
.agency-badge{width:150px;height:38px;background:var(--badge)}
.agency-note{font-size:10.5px;line-height:1.25;width:200px}
.service-lead{font-weight:600;margin-bottom:4px}
.service-cols{display:grid;grid-template-columns:1fr 1fr;gap:16px}
.service-close{text-align:center;margin-top:4px}
.cost-band{position:absolute;left:148px;top:728px;width:670px;height:58px;background:var(--band);display:flex;align-items:center;padding-left:28px;font-size:38px;font-weight:600}
.signs{position:absolute;left:148px;top:796px;width:670px;height:232px;background:var(--band);padding:16px 22px 14px;font-size:14px}
.signs-title{font-family:"Oswald",Arial,sans-serif;font-weight:500;color:var(--flame);font-size:18px;text-transform:uppercase;letter-spacing:.5px;margin-bottom:18px}
.signs ul{list-style:none;display:grid;grid-template-columns:1fr;gap:22px}
.signs li{display:flex;gap:26px}
.signs li span::before{content:"";display:inline-block;width:6px;height:6px;background:var(--flame);margin-right:8px;vertical-align:middle}
.contact{position:absolute;left:148px;top:1068px;width:670px;text-align:right;font-size:17px;color:var(--flame);line-height:1.35}
.contact .email{color:var(--ink)}
.fineprint{position:absolute;left:20px;top:1148px;width:809px;text-align:center;font-size:10px;color:var(--muted);line-height:1.4}
</style>
</head>
<body>
<div class="flyer">
  <div class="scene" role="img" aria-label="Photo of a glowing gas fireplace flame above a family's bare feet warming in front of the fire"></div>

  <header class="header">
    <div class="brand-mark"></div>
    <div class="brand-text">
      <h1 class="brand-name">Merrowind Gas Services</h1>
      <p class="tagline">will be on site conducting gas fireplace safety inspections and maintenance</p>
    </div>
  </header>
  <div class="rule"></div>

  <section class="intro">
    <p>If you wish to have your fireplace serviced, please put your name and unit number on the sign-up sheet provided.</p>
    <p>We will require approximately 20 - 30 minutes to service each fireplace and require that the fireplace is cool to conduct the work.</p>
  </section>

  <section class="service-panel">
    <div class="agency">
      <div class="agency-badge"></div>
      <p class="agency-note">The Hearth Safety Bureau states that all gas fireplaces require regular servicing.</p>
    </div>
    <p class="service-lead">The service Merrowind Gas Services will provide will entail</p>
    <div class="service-cols">
      <p>a thorough assessment of pilot, burner and valve operation, a door seal inspection, repositioning of the logs, an inspection of the electrical circuits,</p>
      <p>testing of fittings for gas leaks, cleaning of the firebox and glass, cleaning and adjustment of fan and controls, a carbon monoxide test,</p>
    </div>
    <p class="service-close">and a complete operational test once the service is complete.</p>
  </section>

  <div class="cost-band">The cost is $60.00 (tax included)</div>

  <section class="signs">
    <h2 class="signs-title">Possible indication that your gas fireplace requires service include:</h2>
    <ul>
      <li><span>Soot build up on glass, logs or exterior of building</span></li>
      <li><span>Main burner is not lighting consistently</span><span>Delayed ignition</span></li>
      <li><span>Strong odors when fireplace is in operation</span><span>Tarnished/discolored brass</span></li>
      <li><span>Flames are not evenly dispersed</span><span>Cloudy film on glass</span><span>Pilot light outages</span></li>
    </ul>
  </section>

  <section class="contact">
    <p>For further information please contact Nadia at: 555.318.4072</p>
    <p>You may also email us at: <span class="email">nadia.merrowindgas@mailbox.com</span></p>
  </section>

  <p class="fineprint">Please do not use your fireplace within 2 hours of your appointment as we do not want the technicians to receive burns.<br>(Owners must have payment ready at time of inspection. Payment may be made in the form of cash, cheque, debit or credit card)</p>
</div>
</body>
</html>
```